International Hand & Body company needing a Hand cream tube design for the Retail market

I am wanting a modern design for a new range of 6 hand creams I will be launching in August. They need to compliment our range of wrapped soaps which you can see on www.plomvane.com.au so am wanting clean designs. I am wanting a solid colour with a hand drawn organic feel line drawing in black elegantly placed wrapping around the label. I am wanting to focus on the colour and positioning of words and fonts. I like modern clean contemporary fonts. The final design needs to appeal to the broader female market.This may lead to range expansion if designs are well received.
Updates

These designs are not hitting the brief. They are too generic and look like a supermarket brand. Our brand is more boutique and this design needs to be modern and simple. I would like more solid colours and more modern designs. Without patterns.

Target Market(s)

Female aged 20 - 70

Requirements
Must have
• a modern contemporary design that will appeal to the masses.
• Please read attached brief.
Should not have
• a black botanical illustration, in a loose and organic design to match the fragrance.

```html
<!DOCTYPE html>
<html lang="en">
<head>
<meta charset="utf-8">
<title>Plomvane Hand Cream Labels</title>
<link href="https://fonts.googleapis.com/css2?family=EB+Garamond&family=Tenor+Sans&display=swap" rel="stylesheet">
<style>
  :root {
    --page: #fdfdfd;
    --ink: #222222;
    --band: #f0f0f0;
    --yuzu: #f9ba0a;
    --sage: #9eb97c;
    --citrus: #ec735c;
    --seagrass: #58a7b1;
    --fig: #9a7d76;
    --sandalwood: #6e6898;
  }
  html, body {
    margin: 0;
    padding: 0;
    width: 1200px;
    height: 829px;
    overflow: hidden;
    background: var(--page);
  }
  .canvas {
    position: relative;
    width: 1200px;
    height: 829px;
  }
  .label {
    position: absolute;
    top: 150px;
    width: 191px;
    height: 525px;
    color: var(--ink);
    text-align: center;
  }
  .label--yuzu { left: 175px; --top-colour: var(--yuzu); --bottom-colour: var(--sage); --split: 236px; }
  .label--citrus { left: 502px; --top-colour: var(--citrus); --bottom-colour: var(--seagrass); --split: 243px; }
  .label--fig { left: 828px; --top-colour: var(--fig); --bottom-colour: var(--sandalwood); --split: 245px; }

  .label__scent {
    position: absolute;
    left: 0; top: 0;
    width: 100%;
    height: var(--split);
    background: var(--top-colour);
    display: flex;
    align-items: center;
    justify-content: center;
    padding-bottom: 10px;
    box-sizing: border-box;
  }
  .label__scent-name {
    margin: 0;
    font-family: "EB Garamond", serif;
    font-weight: 400;
    font-size: 31px;
    line-height: 35px;
  }
  .label__brand-band {
    position: absolute;
    left: 0;
    top: var(--split);
    width: 100%;
    height: 42px;
    background: var(--band);
    display: flex;
    align-items: center;
    justify-content: center;
  }
  .label__brand {
    font-family: "Tenor Sans", sans-serif;
    font-size: 18px;
    letter-spacing: 3px;
  }
  .label__info {
    position: absolute;
    left: 0;
    top: calc(var(--split) + 42px);
    bottom: 0;
    width: 100%;
    background: var(--bottom-colour);
  }
  .label__product {
    position: absolute;
    top: 452px;
    left: 0; width: 100%;
    margin: 0;
    font-family: "Tenor Sans", sans-serif;
    font-weight: 400;
    font-size: 22px;
    line-height: 1;
  }
  .label__description {
    position: absolute;
    top: 355px;
    left: 0; width: 100%;
    margin: 0;
    font-family: "EB Garamond", serif;
    font-size: 19px;
    line-height: 18.3px;
  }
  .label__volume {
    position: absolute;
    top: 467px;
    left: 0; width: 100%;
    margin: 0;
    font-family: "Tenor Sans", sans-serif;
    font-size: 22px;
    line-height: 1;
  }
  .label__origin {
    position: absolute;
    top: 494px;
    left: 0; width: 100%;
    margin: 0;
    font-family: "Tenor Sans", sans-serif;
    font-size: 14px;
    line-height: 1;
  }
  .label .label__product { top: 305px; }
</style>
</head>
<body>
<main class="canvas">
  <article class="label label--yuzu">
    <div class="label__scent"><h2 class="label__scent-name">Yuzu<br>and<br>Sage</h2></div>
    <div class="label__brand-band"><span class="label__brand">plomvane</span></div>
    <div class="label__info"></div>
    <h3 class="label__product">HAND CREAM</h3>
    <p class="label__description">A nourishing<br>non-greasy hand<br>cream to keep skin<br>soft and hydrated</p>
    <p class="label__volume">35ml</p>
    <p class="label__origin">made in Australia</p>
  </article>

  <article class="label label--citrus">
    <div class="label__scent"><h2 class="label__scent-name">Citrus<br>and<br>Seagrass</h2></div>
    <div class="label__brand-band"><span class="label__brand">plomvane</span></div>
    <div class="label__info"></div>
    <h3 class="label__product">HAND CREAM</h3>
    <p class="label__description">A nourishing<br>non-greasy hand<br>cream to keep skin<br>soft and hydrated</p>
    <p class="label__volume">35ml</p>
    <p class="label__origin">made in Australia</p>
  </article>

  <article class="label label--fig">
    <div class="label__scent"><h2 class="label__scent-name">Fig<br>and<br>Sandalwood</h2></div>
    <div class="label__brand-band"><span class="label__brand">plomvane</span></div>
    <div class="label__info"></div>
    <h3 class="label__product">HAND CREAM</h3>
    <p class="label__description">A nourishing<br>non-greasy hand<br>cream to keep skin<br>soft and hydrated</p>
    <p class="label__volume">35ml</p>
    <p class="label__origin">made in Australia</p>
  </article>
</main>
</body>
</html>
```